Kestrel Ledger company needs ad for trade publication

Kestrel Ledgers provides sales, content, production, technology, and promotion products and services to radio stations to help increase sales and solutions to improve operations and reduce costs. We are looking for a creative ad (sizes 720x250, 300x250, 728x180) with a halloween theme. An angle could be "Nothing Scarier than starting the new year in the RED" which in business terms is a net operating loss. OR "Take a bite out of your 2024 budget". Kestrel Ledgers CAN HELP!
We want to highlight on the ad 3 key benefits that Kestrel Ledgers can help (1) "Improve your NTR" (2) "Improve your cash flow" (3) "Improve your technology and operations"
Targeting radio stations during their 2024 budgeting process

```html
<!DOCTYPE html>
<html lang="en">
<head>
<meta charset="utf-8">
<title>Kestrel Ledgers – Nothing Scarier Than Starting the New Year in the Red</title>
<link rel="stylesheet" href="https://fonts.googleapis.com/css2?family=Creepster&family=Jost:wght@400;500;600&display=swap">
<style>
  :root {
    --night-top: #0c1d26;
    --night-mid: #153440;
    --moon-glow: #9fc6cc;
    --ground: #0d1014;
    --chart-glow: #3a0c0e;
    --headline-blue: #1c96f0;
    --headline-white: #ffffff;
    --alarm-red: #f20a0a;
    --arrow-dark: #6e0606;
    --brand-white: #ffffff;
    --benefit-text: #e8eef2;
  }
  html, body {
    margin: 0;
    padding: 0;
    width: 1200px;
    height: 1000px;
    overflow: hidden;
    background: #000;
  }
  .ad {
    position: relative;
    width: 1200px;
    height: 1000px;
    overflow: hidden;
    font-family: "Jost", sans-serif;
  }
  .ad__scene {
    position: absolute;
    inset: 0;
    background:
      radial-gradient(ellipse 170px 150px at 605px 50px, var(--moon-glow) 0%, rgba(159,198,204,0.35) 45%, transparent 100%),
      radial-gradient(ellipse 160px 200px at 905px 300px, rgba(140,70,20,0.35) 0%, transparent 100%),
      radial-gradient(ellipse 380px 120px at 180px 480px, rgba(60,90,110,0.35) 0%, transparent 100%),
      radial-gradient(ellipse 380px 120px at 1030px 500px, rgba(60,90,110,0.3) 0%, transparent 100%),
      radial-gradient(ellipse 600px 230px at 650px 820px, var(--chart-glow) 0%, transparent 100%),
      linear-gradient(180deg, var(--night-top) 0%, var(--night-mid) 22%, #10242c 42%, #151b20 58%, var(--ground) 72%, #0a0b0e 100%);
  }
  .ad__brand {
    position: absolute;
    top: 68px;
    right: 70px;
    margin: 0;
    color: var(--brand-white);
    font-weight: 500;
    font-size: 46px;
    line-height: 0.95;
    text-align: right;
  }
  .ad__loss-arrow {
    position: absolute;
    inset: 0;
    width: 1200px;
    height: 1000px;
  }
  .ad__headline {
    position: absolute;
    left: 0;
    right: 0;
    top: 352px;
    margin: 0;
    text-align: center;
  }
  .ad__headline-lead {
    display: block;
    font-family: "Creepster", cursive;
    font-weight: 400;
    font-size: 88px;
    line-height: 1;
    color: var(--headline-blue);
    transform: scaleY(1.22);
    transform-origin: center top;
  }
  .ad__headline-middle {
    display: block;
    margin-top: 30px;
    margin-left: -10px;
    font-weight: 400;
    font-size: 72px;
    line-height: 1;
    color: var(--headline-white);
  }
  .ad__headline-punch {
    display: block;
    margin-top: 16px;
    margin-left: -20px;
    font-family: "Creepster", cursive;
    font-weight: 400;
    font-size: 112px;
    line-height: 1;
    color: var(--alarm-red);
    transform: scaleY(1.15);
    transform-origin: center top;
  }
  .ad__benefits {
    position: absolute;
    left: 70px;
    right: 70px;
    top: 818px;
    margin: 0;
    padding: 0;
    list-style: none;
    display: flex;
    justify-content: space-between;
    gap: 24px;
  }
  .ad__benefit {
    flex: 1;
    display: flex;
    align-items: center;
    gap: 12px;
    color: var(--benefit-text);
    font-weight: 500;
    font-size: 24px;
    line-height: 1.15;
  }
  .ad__benefit-tick {
    flex: none;
    width: 34px;
    height: 34px;
  }
  .ad__cta {
    position: absolute;
    left: 0;
    right: 0;
    top: 912px;
    margin: 0;
    text-align: center;
    color: var(--headline-white);
    font-weight: 600;
    font-size: 40px;
    line-height: 1;
  }
  .ad__cta-accent {
    color: var(--headline-blue);
  }
</style>
</head>
<body>
  <main class="ad">
    <div class="ad__scene" role="img" aria-label="Night scene: full moon behind stormy clouds, a haunted house with lit windows, misty graveyard with tombstones, and a blurred red falling stock-market chart across the lower half"></div>

    <p class="ad__brand">Kestrel<br>Ledgers</p>

    <svg class="ad__loss-arrow" viewBox="0 0 1200 1000" aria-hidden="true">
      <defs>
        <linearGradient id="lossArrowFill" x1="817" y1="594" x2="1117" y2="794" gradientUnits="userSpaceOnUse">
          <stop offset="0" stop-color="#5a0505" stop-opacity="0.6"/>
          <stop offset="0.5" stop-color="#a00606"/>
          <stop offset="1" stop-color="#f20a0a"/>
        </linearGradient>
      </defs>
      <polyline points="817,600 920,718 974,670 1050,732" fill="none" stroke="url(#lossArrowFill)" stroke-width="38" stroke-linejoin="miter"/>
      <polygon points="1008,766 1088,688 1117,794" fill="#f20a0a"/>
    </svg>

    <h1 class="ad__headline">
      <span class="ad__headline-lead">NOTHING SCARIER THAN</span>
      <span class="ad__headline-middle">Starting the New Year</span>
      <span class="ad__headline-punch">IN THE RED</span>
    </h1>

    <ul class="ad__benefits">
      <li class="ad__benefit">
        <svg class="ad__benefit-tick" viewBox="0 0 34 34" aria-hidden="true"><circle cx="17" cy="17" r="16" fill="#1c96f0"/><path d="M9 17.5l5.5 5.5L25 12" fill="none" stroke="#fff" stroke-width="3.5" stroke-linecap="round" stroke-linejoin="round"/></svg>
        <span>Improve your NTR</span>
      </li>
      <li class="ad__benefit">
        <svg class="ad__benefit-tick" viewBox="0 0 34 34" aria-hidden="true"><circle cx="17" cy="17" r="16" fill="#1c96f0"/><path d="M9 17.5l5.5 5.5L25 12" fill="none" stroke="#fff" stroke-width="3.5" stroke-linecap="round" stroke-linejoin="round"/></svg>
        <span>Improve your cash flow</span>
      </li>
      <li class="ad__benefit">
        <svg class="ad__benefit-tick" viewBox="0 0 34 34" aria-hidden="true"><circle cx="17" cy="17" r="16" fill="#1c96f0"/><path d="M9 17.5l5.5 5.5L25 12" fill="none" stroke="#fff" stroke-width="3.5" stroke-linecap="round" stroke-linejoin="round"/></svg>
        <span>Improve your technology<br>and operations</span>
      </li>
    </ul>

    <p class="ad__cta"><span class="ad__cta-accent">Kestrel Ledgers</span> CAN HELP!</p>
  </main>
</body>
</html>
```